Business Card and Letterhead for new company Vardel GreenWorks, Inc.

Vardel GreenWorks, Inc., an engineering and construction firm that provides services for solid waste landfill gas systems, needs a business card and letterhead. We recently had a logo designed but we are open to some tweaks to logo design and color scheme. Generally, we like "earthy" color tones - greens, browns, oranges. This is a sister company - www.talvoriengineering.example.

Target Market(s)

Solid waste landfill companies - Brindle Disposal, Halcott Hauling, etc.

Industry/Entity Type

Engineering and Construction

Contact Information for Business Card

Name, Title, email, mobile phone, work phone, website. Potential list of services for back of card: LFG Engineering and Design, GCCS Planning and Operational Consulting, Compliance Monitoring and Reporting, Routine Operations & Maintenance, Nonroutine O&M, Construction Management, Construction QA, GCCS Construction

Font styles to use
Sans Serif

Requirements
Must have
• Logo, pertinent information, maybe a tagline (still in development)
Nice to have
• For back of card, considering an engineering scale (attached for another business of ours), but want to look at other options, alternatives. Like the idea of the back of card to have some utility (scale, unit conversion info, list of services) but willing to consider lots of options.
Should not have
• Needs to have a professional (engineering) and technical look, not cartoonish.

```html
<!DOCTYPE html>
<html lang="en">
<head>
<meta charset="utf-8">
<title>Vardel GreenWorks – Letterhead and Business Card</title>
<link rel="stylesheet" href="https://fonts.googleapis.com/css2?family=Public+Sans:ital,wght@0,400;0,600;0,700;1,400&display=swap">
<style>
  :root{
    --green:#6db33f;
    --earth:#6b5f43;
    --ink:#2c2c2c;
    --muted:#6f6f6f;
    --paper:#ffffff;
    --stage-left:#a7a8ab;
    --stage-right:#a8b2c3;
    --mark:#3a9ad1;
    --ghost:#eeeeee;
  }
  *{box-sizing:border-box;margin:0;padding:0}
  html,body{width:1200px;height:900px;overflow:hidden}
  body{font-family:"Public Sans",Arial,sans-serif;color:var(--ink);position:relative}
  .stage{position:absolute;top:0;height:900px}
  .stage--left{left:0;width:700px;background:var(--stage-left)}
  .stage--right{left:700px;width:500px;background:var(--stage-right)}

  /* Letterhead */
  .letterhead{position:absolute;width:425px;height:600px;background:var(--paper);transform-origin:0 0;overflow:hidden}
  .letterhead--a{left:139px;top:82px}
  .letterhead--b{left:732px;top:58px;transform:scale(1.047)}
  .letterhead__bar{position:absolute;left:0;top:0;width:30px;height:497px;background:var(--green)}
  .letterhead__bar--earth{top:497px;height:103px;background:var(--earth)}
  .brand{position:absolute;display:flex;align-items:center;gap:5px}
  .brand__dot{width:13px;height:13px;border-radius:50%;background:var(--green);flex:none}
  .brand__name{font-weight:700;color:var(--green);letter-spacing:.4px;line-height:1.05;text-transform:uppercase}
  .letterhead .brand{left:52px;top:46px}
  .letterhead .brand__name{font-size:11px}
  .ghost-disc{position:absolute;border-radius:50%;background:var(--ghost)}
  .letterhead .ghost-disc{left:282px;top:30px;width:120px;height:120px;opacity:.75}
  .meta{position:absolute;left:55px;right:27px;font-size:7.5px}
  .meta__row{display:flex;justify-content:space-between}
  .meta--labels{top:124px}
  .meta--names{top:144px;font-weight:700}
  .recipient-role{position:absolute;left:55px;top:159px;font-size:7.5px;line-height:10px}
  .body{position:absolute;left:55px;right:27px;top:206px;font-size:7.4px;line-height:10.3px;text-align:justify}
  .body p{margin-bottom:10.3px}
  .signoff{position:absolute;right:62px;top:451px;font-size:7.5px;line-height:10.5px;text-align:right}
  .footer{position:absolute;left:55px;top:545px;font-size:5.8px;color:var(--muted);line-height:10.5px}
  .footer__company{padding-left:15px}
  .footer__line{display:flex;align-items:center;gap:6px}
  .footer__line svg{width:8px;height:8px;fill:var(--green);flex:none}

  /* Business card */
  .card{position:absolute;height:124px;overflow:hidden}
  .card--front{width:204px;background:var(--paper)}
  .card--front-a{left:139px;top:695px}
  .card--front-b{left:732px;top:720px;transform:scale(1.02,1.02);transform-origin:0 0}
  .card__strip{position:absolute;right:0;top:0;width:4px;height:106px;background:var(--green)}
  .card__strip--earth{top:106px;height:18px;background:var(--earth)}
  .card--front .brand{left:10px;top:14px;gap:4px}
  .card--front .brand__dot{width:10px;height:10px}
  .card--front .brand__name{font-size:7px}
  .card--front .ghost-disc{left:8px;top:54px;width:64px;height:64px}
  .card__person{position:absolute;right:14px;top:48px;text-align:right}
  .card__name{font-size:8.5px;font-weight:600;color:var(--green)}
  .card__title{font-size:4.6px;font-style:italic;color:var(--muted);margin-top:1px}
  .card__contacts{position:absolute;right:14px;top:78px;font-size:4.6px;color:var(--muted);line-height:9.2px;text-align:right}
  .card__contacts div{display:flex;justify-content:flex-end;align-items:center;gap:6px}
  .card__contacts svg{width:5px;height:5px;fill:var(--green)}

  .card--back{background:var(--earth);color:#fff}
  .card--back-a{left:357px;top:695px;width:206px}
  .card--back-b{left:962px;top:720px;width:194px;height:126px}
  .services{position:absolute;left:20px;top:17px}
  .services__title{font-size:8px;color:var(--green);letter-spacing:.3px;margin-bottom:5px}
  .services__list{list-style:none;font-size:5px;line-height:9.1px}
  .services__list li::before{content:"• "}
  .scale{position:absolute;right:4px;top:4px;width:26px;height:116px}
</style>
</head>
<body>
  <div class="stage stage--left"></div>
  <div class="stage stage--right"></div>

  <!-- Letterhead, presentation size -->
  <section class="letterhead letterhead--a" aria-label="Letterhead">
    <div class="letterhead__bar"></div>
    <div class="letterhead__bar letterhead__bar--earth"></div>
    <div class="ghost-disc"></div>
    <div class="brand"><span class="brand__dot"></span><span class="brand__name">Vardel<br>GreenWorks</span></div>
    <div class="meta meta--labels"><div class="meta__row"><span>TO :</span><span>DATE :</span></div></div>
    <div class="meta meta--names"><div class="meta__row"><span>Mr. Smith</span><span>AUGUST 18, 2024</span></div></div>
    <div class="recipient-role">Marketing Manager<br>Company</div>
    <div class="body">
      <p>Lorem ipsum dolor sit amet, consectetuer adipiscing elit, sed diam nonummy nibh euismod tincidunt ut laoreet dolore magna aliquam erat volutpat. Ut wisi enim ad minim veniam, quis nostrud exerci tation ullamcorper suscipit lobortis nisl ut aliquip ex ea commodo consequat. Duis autem vel eum iriure dolor in hendrerit in vulputate velit esse molestie consequat, vel illum dolore eu feugiat nulla facilisis at vero eros et accumsan et iusto odio dignissim qui blandit praesent luptatum zzril delenit augue duis dolore te feugait nulla facilisi.</p>
      <p>Lorem ipsum dolor sit amet, cons ectetuer adipiscing elit, sed diam nonummy nibh euismod tincidunt ut laoreet dolore magna aliquam erat volutpat. Ut wisi enim ad minim veniam, quis nostrud exerci tation ullamcorper suscipit lobortis nisl ut aliquip ex ea commodo consequat.</p>
      <p>Lorem ipsum dolor sit amet, consectetuer adipiscing elit, sed diam nonummy nibh euismod tincidunt ut laoreet dolore magna aliquam erat volutpat. Ut wisi enim ad minim veniam, quis nostrud exerci tation ullamcorper suscipit lobortis nisl ut aliquip ex ea commodo consequat. Duis autem vel eum iriure dolor in hendrerit in vulputate velit esse molestie consequat, vel illum dolore eu feugiat nulla facilisis at vero eros et accumsan et iusto odio dignissim qui blandit praesent luptatum zzril delenit augue duis dolore te feugait nulla facilisi.veniam, quis nostrud exerci tation ullamcorper suscipit lobortis nisl ut aliquip ex ea commodo consequat.</p>
    </div>
    <div class="signoff">Sincerly,<br>HRD Manager</div>
    <div class="footer">
      <div class="footer__company">Vardel GreenWorks, Inc.</div>
      <div class="footer__line"><svg viewBox="0 0 10 10"><path d="M5 0a3.6 3.6 0 0 0-3.6 3.6C1.4 6.3 5 10 5 10s3.6-3.7 3.6-6.4A3.6 3.6 0 0 0 5 0zm0 5a1.4 1.4 0 1 1 0-2.8A1.4 1.4 0 0 1 5 5z"/></svg>4870 Ridgeline Parkway, Suite 210, Brookfield, TN, 37999, United States</div>
      <div class="footer__line"><svg viewBox="0 0 10 10"><path d="M2 0l2 2.4-1.2 1.4a6 6 0 0 0 3.4 3.4L7.6 6 10 8l-1.4 2C4 10 0 6 0 1.4z"/></svg>555-014-2270</div>
      <div class="footer__line"><svg viewBox="0 0 10 10"><circle cx="5" cy="5" r="5"/></svg>www.vardelgreenworks.example</div>
    </div>
  </section>

  <!-- Letterhead, larger presentation -->
  <section class="letterhead letterhead--b" aria-label="Letterhead">
    <div class="letterhead__bar"></div>
    <div class="letterhead__bar letterhead__bar--earth"></div>
    <div class="ghost-disc"></div>
    <div class="brand"><span class="brand__dot"></span><span class="brand__name">Vardel<br>GreenWorks</span></div>
    <div class="meta meta--labels"><div class="meta__row"><span>TO :</span><span>DATE :</span></div></div>
    <div class="meta meta--names"><div class="meta__row"><span>Mr. Smith</span><span>AUGUST 18, 2024</span></div></div>
    <div class="recipient-role">Marketing Manager<br>Company</div>
    <div class="body">
      <p>Lorem ipsum dolor sit amet, consectetuer adipiscing elit, sed diam nonummy nibh euismod tincidunt ut laoreet dolore magna aliquam erat volutpat. Ut wisi enim ad minim veniam, quis nostrud exerci tation ullamcorper suscipit lobortis nisl ut aliquip ex ea commodo consequat. Duis autem vel eum iriure dolor in hendrerit in vulputate velit esse molestie consequat, vel illum dolore eu feugiat nulla facilisis at vero eros et accumsan et iusto odio dignissim qui blandit praesent luptatum zzril delenit augue duis dolore te feugait nulla facilisi.</p>
      <p>Lorem ipsum dolor sit amet, cons ectetuer adipiscing elit, sed diam nonummy nibh euismod tincidunt ut laoreet dolore magna aliquam erat volutpat. Ut wisi enim ad minim veniam, quis nostrud exerci tation ullamcorper suscipit lobortis nisl ut aliquip ex ea commodo consequat.</p>
      <p>Lorem ipsum dolor sit amet, consectetuer adipiscing elit, sed diam nonummy nibh euismod tincidunt ut laoreet dolore magna aliquam erat volutpat. Ut wisi enim ad minim veniam, quis nostrud exerci tation ullamcorper suscipit lobortis nisl ut aliquip ex ea commodo consequat. Duis autem vel eum iriure dolor in hendrerit in vulputate velit esse molestie consequat, vel illum dolore eu feugiat nulla facilisis at vero eros et accumsan et iusto odio dignissim qui blandit praesent luptatum zzril delenit augue duis dolore te feugait nulla facilisi.veniam, quis nostrud exerci tation ullamcorper suscipit lobortis nisl ut aliquip ex ea commodo consequat.</p>
    </div>
    <div class="signoff">Sincerly,<br>HRD Manager</div>
    <div class="footer">
      <div class="footer__company">Vardel GreenWorks, Inc.</div>
      <div class="footer__line"><svg viewBox="0 0 10 10"><path d="M5 0a3.6 3.6 0 0 0-3.6 3.6C1.4 6.3 5 10 5 10s3.6-3.7 3.6-6.4A3.6 3.6 0 0 0 5 0zm0 5a1.4 1.4 0 1 1 0-2.8A1.4 1.4 0 0 1 5 5z"/></svg>4870 Ridgeline Parkway, Suite 210, Brookfield, TN, 37999, United States</div>
      <div class="footer__line"><svg viewBox="0 0 10 10"><path d="M2 0l2 2.4-1.2 1.4a6 6 0 0 0 3.4 3.4L7.6 6 10 8l-1.4 2C4 10 0 6 0 1.4z"/></svg>555-014-2270</div>
      <div class="footer__line"><svg viewBox="0 0 10 10"><circle cx="5" cy="5" r="5"/></svg>www.vardelgreenworks.example</div>
    </div>
  </section>

  <!-- Business card fronts -->
  <section class="card card--front card--front-a" aria-label="Business card front">
    <div class="card__strip"></div><div class="card__strip card__strip--earth"></div>
    <div class="ghost-disc"></div>
    <div class="brand"><span class="brand__dot"></span><span class="brand__name">Vardel<br>GreenWorks</span></div>
    <div class="card__person"><div class="card__name">Dorian K. Halvey, PE</div><div class="card__title">President, Principal Engineer</div></div>
    <div class="card__contacts">
      <div>555-014-2270<svg viewBox="0 0 10 10"><path d="M2 0l2 2.4-1.2 1.4a6 6 0 0 0 3.4 3.4L7.6 6 10 8l-1.4 2C4 10 0 6 0 1.4z"/></svg></div>
      <div>555-019-4381<svg viewBox="0 0 10 10"><rect x="2" y="0" width="6" height="10" rx="1"/></svg></div>
      <div>dhalvey@vardelgreenworks.example<svg viewBox="0 0 10 10"><rect x="0" y="2" width="10" height="6"/></svg></div>
      <div>www.vardelgreenworks.example<svg viewBox="0 0 10 10"><circle cx="5" cy="5" r="5"/></svg></div>
    </div>
  </section>

  <section class="card card--front card--front-b" aria-label="Business card front">
    <div class="card__strip"></div><div class="card__strip card__strip--earth"></div>
    <div class="ghost-disc"></div>
    <div class="brand"><span class="brand__dot"></span><span class="brand__name">Vardel<br>GreenWorks</span></div>
    <div class="card__person"><div class="card__name">Dorian K. Halvey, PE</div><div class="card__title">President, Principal Engineer</div></div>
    <div class="card__contacts">
      <div>555-014-2270<svg viewBox="0 0 10 10"><path d="M2 0l2 2.4-1.2 1.4a6 6 0 0 0 3.4 3.4L7.6 6 10 8l-1.4 2C4 10 0 6 0 1.4z"/></svg></div>
      <div>555-019-4381<svg viewBox="0 0 10 10"><rect x="2" y="0" width="6" height="10" rx="1"/></svg></div>
      <div>dhalvey@vardelgreenworks.example<svg viewBox="0 0 10 10"><rect x="0" y="2" width="10" height="6"/></svg></div>
      <div>www.vardelgreenworks.example<svg viewBox="0 0 10 10"><circle cx="5" cy="5" r="5"/></svg></div>
    </div>
  </section>

  <!-- Business card backs -->
  <section class="card card--back card--back-a" aria-label="Business card back">
    <div class="services">
      <div class="services__title">SERVICES</div>
      <ul class="services__list">
        <li>LFG Engineering and Design</li>
        <li>GCCS Planning and Operational Consulting</li>
        <li>Compliance Monitoring and Reporting</li>
        <li>Routine Operations &amp; Maintenance</li>
        <li>Nonroutine O&amp;M</li>
        <li>Construction Management</li>
        <li>Construction QA</li>
        <li>GCCS Construction</li>
      </ul>
    </div>
    <svg class="scale" viewBox="0 0 26 116" aria-label="Engineering scale">
      <defs>
        <pattern id="ticks-a" width="26" height="2.3" patternUnits="userSpaceOnUse">
          <line x1="18" y1="0.5" x2="26" y2="0.5" stroke="#fff" stroke-width="0.4"/>
        </pattern>
      </defs>
      <rect x="0" y="0" width="26" height="116" fill="url(#ticks-a)"/>
      <g stroke="#fff" stroke-width="0.5">
        <line x1="12" y1="5" x2="26" y2="5"/><line x1="12" y1="28" x2="26" y2="28"/><line x1="12" y1="51" x2="26" y2="51"/><line x1="12" y1="74" x2="26" y2="74"/><line x1="12" y1="97" x2="26" y2="97"/>
      </g>
      <g fill="#fff" font-size="3" font-family="Public Sans, sans-serif">
        <text x="4" y="7">0</text><text x="3" y="30">10</text><text x="3" y="53">20</text><text x="3" y="76">30</text><text x="3" y="99">40</text>
      </g>
    </svg>
  </section>

  <section class="card card--back card--back-b" aria-label="Business card back">
    <div class="services">
      <div class="services__title">SERVICES</div>
      <ul class="services__list">
        <li>LFG Engineering and Design</li>
        <li>GCCS Planning and Operational Consulting</li>
        <li>Compliance Monitoring and Reporting</li>
        <li>Routine Operations &amp; Maintenance</li>
        <li>Nonroutine O&amp;M</li>
        <li>Construction Management</li>
        <li>Construction QA</li>
        <li>GCCS Construction</li>
      </ul>
    </div>
    <svg class="scale" viewBox="0 0 26 116" aria-label="Engineering scale">
      <defs>
        <pattern id="ticks-b" width="26" height="2.3" patternUnits="userSpaceOnUse">
          <line x1="18" y1="0.5" x2="26" y2="0.5" stroke="#fff" stroke-width="0.4"/>
        </pattern>
      </defs>
      <rect x="0" y="0" width="26" height="116" fill="url(#ticks-b)"/>
      <g stroke="#fff" stroke-width="0.5">
        <line x1="12" y1="5" x2="26" y2="5"/><line x1="12" y1="28" x2="26" y2="28"/><line x1="12" y1="51" x2="26" y2="51"/><line x1="12" y1="74" x2="26" y2="74"/><line x1="12" y1="97" x2="26" y2="97"/>
      </g>
      <g fill="#fff" font-size="3" font-family="Public Sans, sans-serif">
        <text x="4" y="7">0</text><text x="3" y="30">10</text><text x="3" y="53">20</text><text x="3" y="76">30</text><text x="3" y="99">40</text>
      </g>
    </svg>
  </section>
</body>
</html>
```